Paint Factory Needs Bucket Designs

I have paint factory and I want Paint buckets designs. The buckets should be the below sizes:

1 ltr
4 ltrs
10 ltrs
20 ltrs

```html
<!DOCTYPE html>
<html lang="en">
<head>
<meta charset="utf-8">
<title>Hueline Paint Bucket Label – 4 LTR</title>
<link rel="stylesheet" href="https://fonts.googleapis.com/css2?family=Montserrat:wght@600;700;800;900&family=Courgette&display=swap">
<style>
  :root {
    --page-bg: #f4f4f9;
    --label-white: #ececec;
    --ink-dark: #2b2b2b;
    --panel-dark-start: #161616;
    --panel-dark-end: #8c8c8c;
    --teal: #4fb8b4;
    --teal-deep: #0f5c5a;
    --teal-light: #72cfca;
    --text-light: #e6e6e6;
  }
  * { margin: 0; padding: 0; box-sizing: border-box; }
  html, body {
    width: 1094px;
    height: 1200px;
    overflow: hidden;
    background: var(--page-bg);
  }
  .canvas {
    position: relative;
    width: 1094px;
    height: 1200px;
  }
  .bucket-label {
    position: absolute;
    left: 97px;
    top: 120px;
    width: 900px;
    height: 960px;
    background: var(--label-white);
    box-shadow: 0 10px 40px rgba(40, 40, 70, 0.12);
    overflow: hidden;
  }
  .label-shapes {
    position: absolute;
    inset: 0;
  }
  .brand-name {
    position: absolute;
    left: 300px;
    width: 300px;
    top: 150px;
    text-align: center;
    font-family: "Montserrat", sans-serif;
    font-weight: 800;
    font-size: 56px;
    letter-spacing: 1px;
    color: var(--ink-dark);
  }
  .product-title {
    position: absolute;
    left: 0;
    width: 900px;
    top: 300px;
    text-align: center;
    font-family: "Montserrat", sans-serif;
    font-weight: 900;
    font-size: 112px;
    line-height: 1;
    letter-spacing: 2px;
    color: var(--teal);
  }
  .product-subtitle {
    position: absolute;
    left: 0;
    width: 900px;
    top: 440px;
    text-align: center;
    font-family: "Montserrat", sans-serif;
    font-weight: 700;
    font-size: 56px;
    letter-spacing: 2px;
    color: var(--text-light);
  }
  .title-rule {
    position: absolute;
    left: 270px;
    width: 360px;
    top: 535px;
    height: 2px;
    background: var(--text-light);
    opacity: 0.85;
  }
  .tagline {
    position: absolute;
    left: 0;
    width: 900px;
    top: 630px;
    text-align: center;
    font-family: "Courgette", cursive;
    font-size: 40px;
    color: var(--teal);
  }
  .volume-badge {
    position: absolute;
    left: 385px;
    top: 800px;
    width: 130px;
    height: 130px;
    border-radius: 50%;
    background: var(--label-white);
    border: 6px solid var(--teal);
    display: flex;
    flex-direction: column;
    align-items: center;
    justify-content: center;
    font-family: "Montserrat", sans-serif;
  }
  .volume-number {
    font-weight: 900;
    font-size: 58px;
    line-height: 0.95;
    color: var(--teal);
  }
  .volume-unit {
    font-weight: 800;
    font-size: 20px;
    letter-spacing: 1px;
    color: var(--ink-dark);
  }
</style>
</head>
<body>
<main class="canvas">
  <section class="bucket-label">
    <svg class="label-shapes" width="900" height="960" viewBox="0 0 900 960" aria-hidden="true">
      <defs>
        <linearGradient id="panelShade" x1="0" y1="0" x2="1" y2="0">
          <stop offset="0" stop-color="#161616"/>
          <stop offset="0.5" stop-color="#3a3a3a"/>
          <stop offset="1" stop-color="#8c8c8c"/>
        </linearGradient>
        <linearGradient id="tealBand" x1="0" y1="0" x2="1" y2="0">
          <stop offset="0" stop-color="#0f5c5a"/>
          <stop offset="0.5" stop-color="#2f9995"/>
          <stop offset="1" stop-color="#72cfca"/>
        </linearGradient>
      </defs>
      <path class="dark-panel" fill="url(#panelShade)"
            d="M0 70 L300 100 L300 250 L340 290 L560 290 L600 250 L600 100 L900 60 L900 960 L0 960 Z"/>
      <path class="teal-band" fill="url(#tealBand)"
            d="M0 770 Q450 900 900 760 L900 960 L0 960 Z"/>
    </svg>

    <div class="brand-name">HUELINE</div>
    <h1 class="product-title">LOREM IPSUM</h1>
    <h2 class="product-subtitle">LOREM IPSUM DOLOR</h2>
    <div class="title-rule"></div>
    <p class="tagline">Make your home beautifull</p>

    <div class="volume-badge">
      <span class="volume-number">4</span>
      <span class="volume-unit">LTR</span>
    </div>
  </section>
</main>
</body>
</html>
```